An envelope for Housekeepers / The Marigold Sleeve

Globally, 212 million people are employed in the hospitality industry. While many get commemorated for their work, there is one job that is often looked over.
Housekeepers hardly ever get told how great of a job they are doing.
Our company QuillNestly is seeking to empower housekeepers by allowing our guests to tip them through a cool envelope.
The plan :
- Create an envelope that has a message on it, which will incentivize our clientele to tip their housekeepers at check-out, and give housekeepers the credit they deserve for their hard work.
Example :
- "Humans do well by doing good" / "a thank you for your housekeeper"
What to do :
- Create an envelope based on the attached file. The white page titled "The Marigold Sleeve" will be the front of the envelope (feel free to improve it but we really like the concept of it). The four blue pages will be the back pages of the envelope. Feel free to scour the web for quotes & embodying the same message of generosity.
We are really looking forward to seeing what kind of creative envelope you can conjure.
PS : remember that the goal with this envelope is to empower housekeepers & incentivize guests to tip them.
Target Market(s)
Travelers & housekeepers
Industry/Entity Type
Hospitality
Other font styles liked:
- Trebuchet, Times New Roman
Requirements
Must have
- Our project must have :
- - A white first page titled "The Marigold Sleev" is a must
- - You can improve it, but do not change the concept of it
- - Font : simple & easy to read
- - Color of back page : Teal
Nice to have
- Always keep in mind that this envelope is made to empower housekeepers.
Should not have
- Just keep it simple. Don't complicate things.

```html
<!DOCTYPE html>
<html lang="en">
<head>
<meta charset="utf-8">
<title>The Marigold Sleeve — Front &amp; Back Envelope</title>
<link rel="stylesheet" href="https://fonts.googleapis.com/css2?family=Montserrat:wght@300;400;600;700&family=Allura&display=swap">
<style>
  :root {
    --teal: #04a88e;
    --teal-bright: #14c3a7;
    --mint: #b0e2df;
    --slate: #787882;
    --ink: #5b5a5e;
    --paper: #ffffff;
    --heading: #0aa58d;
  }
  * { margin: 0; padding: 0; box-sizing: border-box; }
  html, body { width: 1200px; height: 1200px; overflow: hidden; background: var(--paper); }
  .canvas { position: relative; width: 1200px; height: 1200px; font-family: "Montserrat", Arial, sans-serif; }

  .sheet-title {
    position: absolute; top: 72px; left: 0; width: 1200px; text-align: center;
    font-weight: 400; font-size: 32px; letter-spacing: 0.2em; color: var(--heading);
  }
  .stage { position: absolute; top: 138px; left: 0; width: 1200px; height: 936px; background: var(--slate); }

  .dieline { position: absolute; top: 0; left: 0; width: 1200px; height: 1200px; }

  .back-panel { position: absolute; left: 149px; top: 180px; width: 513px; height: 730px; background: var(--teal); }
  .quote {
    position: absolute; top: 210px; left: 0; width: 100%; text-align: center;
    color: var(--mint); font-size: 58px; line-height: 76px; letter-spacing: -0.01em;
  }
  .quote strong { font-weight: 600; }
  .quote .light { font-weight: 300; }
  .quote-author {
    position: absolute; top: 392px; left: 0; width: 100%; text-align: center;
    font-family: "Allura", cursive; font-size: 64px; color: var(--mint);
  }
  .thanks-band {
    position: absolute; top: 532px; left: 0; width: 100%; height: 42px; background: var(--teal-bright);
    display: flex; align-items: center; justify-content: center;
    color: var(--mint); font-size: 14px; letter-spacing: 0.3em; font-weight: 400;
  }

  .brand { position: absolute; display: flex; align-items: center; gap: 14px; color: var(--ink); }
  .brand-dot { width: 58px; height: 58px; border-radius: 50%; border: 4px solid var(--ink); }
  .brand-name { font-weight: 400; font-size: 25px; line-height: 25px; letter-spacing: 0.01em; }
  .back-panel .brand { left: 168px; top: 628px; }

  .front-panel { position: absolute; left: 664px; top: 180px; width: 515px; height: 730px; background: var(--paper); }
  .front-title {
    position: absolute; top: 190px; left: 0; width: 100%; text-align: center;
    color: var(--mint); font-weight: 700; font-size: 52px; line-height: 76px;
  }
  .front-by {
    position: absolute; top: 488px; left: 0; width: 100%; text-align: center;
    color: var(--mint); font-size: 17px; font-weight: 400;
  }
  .front-panel .brand { left: 169px; top: 573px; }
</style>
</head>
<body>
<div class="canvas">
  <h1 class="sheet-title">FRONT-BACK ENVELOPE</h1>
  <div class="stage"></div>

  <svg class="dieline" viewBox="0 0 1200 1200" aria-hidden="true">
    <polygon class="side-flap" points="150,180 42,240 46,836 150,912" fill="#b0e2df"/>
    <polygon class="bottom-flap" points="146,910 662,910 580,1030 146,1030" fill="#b0e2df"/>
  </svg>

  <section class="back-panel">
    <p class="quote"><strong>“KINDNESS</strong> <span class="light">has</span><br><span class="light">no</span> <strong>PRICE.”</strong></p>
    <p class="quote-author">Lorna Vale</p>
    <div class="thanks-band">A THANK YOU FOR YOUR HOUSEKEEPER</div>
    <div class="brand">
      <span class="brand-dot"></span>
      <span class="brand-name">QUILL<br>NESTLY</span>
    </div>
  </section>

  <section class="front-panel">
    <svg class="accent-lines" width="515" height="730" viewBox="0 0 515 730" style="position:absolute;left:0;top:0" aria-hidden="true">
      <rect x="6" y="24" width="5" height="436" fill="#04a88e"/>
      <rect x="15" y="24" width="3" height="306" fill="#04a88e"/>
      <rect x="506" y="264" width="5" height="436" fill="#04a88e"/>
      <rect x="500" y="394" width="3" height="306" fill="#04a88e"/>
    </svg>
    <h2 class="front-title">The<br>Marigold<br>Sleeve</h2>
    <p class="front-by">BY</p>
    <div class="brand">
      <span class="brand-dot"></span>
      <span class="brand-name">QUILL<br>NESTLY</span>
    </div>
  </section>
</div>
</body>
</html>
```